Bramblewick Co Leaflet. A5 2-sided Flyer for a UK Lawn Treatment Company

I need an A5 two-side leaflet / flyer designed for my Lawn Treatment company. The leaflet will be for door-drops so quick impact needed. Full colour, both sides. I provide lawn treatments to customers in the Exeter area of Devon. I would like to design to be clear, fresh and reflect the joy a good lawn and garden can bring.

Target Market(s)

Home Owners. 30-80 Years. Familys

Font styles to use
Sans Serif

Colors
9bcb3c
f78f20
ec1f27
33a6d7

Requirements
Must have
• Good front page picture
• Logo
• Contact details on front.
• Call to Action
• More details in Text file included in design.
Nice to have
• Clipart of a family / lady enjoying a lawn.

```html
<!DOCTYPE html>
<html lang="en">
<head>
<meta charset="utf-8">
<title>Bramblewick Co Leaflet</title>
<link href="https://fonts.googleapis.com/css2?family=Asap:wght@400;600;700&family=Oswald:wght@500&family=Questrial&display=swap" rel="stylesheet">
<style>
:root{
  --bg:#dcdcdc;
  --green:#1e8c1e;
  --green-dark:#176b17;
  --blue:#2a6db5;
  --brown:#5b1c10;
  --yellow:#f7b81c;
  --yellow-light:#fcd86a;
  --grey-band:#ececec;
  --text:#444;
  --white:#fff;
}
*{margin:0;padding:0;box-sizing:border-box}
html,body{width:1200px;height:858px;overflow:hidden;background:var(--bg)}
body{position:relative;font-family:'Questrial',sans-serif;color:var(--text)}
.page{position:absolute;top:54px;width:508px;height:720px;background:var(--white);overflow:hidden}
.page--front{left:66px}
.page--back{left:627px}
.abs{position:absolute}
.center{left:0;right:0;text-align:center}
.photo{position:absolute;background:linear-gradient(180deg,#c9d8b0 0%,#6f9a48 35%,#5fa03a 70%,#7dbb43 100%)}

/* front */
.front-photo{left:0;top:0;width:508px;height:360px}
.front-waves{position:absolute;left:0;top:220px}
.brand-front{top:372px;left:0;right:0;display:flex;align-items:center;justify-content:center;gap:12px}
.brand-dot{width:34px;height:34px;border-radius:50%;background:var(--green)}
.brand-name{font-family:'Asap',sans-serif;font-weight:600;font-size:40px;color:var(--green);white-space:nowrap}
.rule{position:absolute;left:43px;width:434px;height:2px;background:#bdbdbd}
.tagline{font-family:'Asap',sans-serif;font-size:24px;line-height:28px;white-space:nowrap}
.tagline .blue{color:var(--blue)}
.tagline .brown{color:var(--brown)}
.new-area{top:505px;font-family:'Asap',sans-serif;font-weight:700;font-size:21px;color:var(--blue)}
.pill{position:absolute;border-radius:12px;background:linear-gradient(180deg,var(--yellow-light) 0%,var(--yellow) 55%,#f3a812 100%);border:2px solid #e0c88a;text-align:center;font-family:'Asap',sans-serif;color:var(--brown);white-space:nowrap}
.exp-pill{left:71px;top:538px;width:365px;height:52px;padding-top:5px;font-size:18px;line-height:21px}
.exp-pill b{font-weight:700}
.seal{position:absolute;left:14px;top:596px;width:108px;height:108px;border-radius:50%;background:var(--green)}
.seal::after{content:"";position:absolute;left:12px;top:12px;width:84px;height:84px;border-radius:50%;background:#8a1a1a}
.contact{position:absolute;left:160px;top:604px;display:flex;gap:8px;align-items:center}
.contact-lines{font-family:'Asap',sans-serif;font-size:16px;line-height:18px;color:var(--blue);white-space:nowrap}
.contact-lines b{color:var(--green);font-weight:700}
.front-foot{position:absolute;left:0;top:640px}
.book{top:684px;left:60px;right:0;color:var(--white);font-family:'Asap',sans-serif;font-weight:700;font-size:15px}
.web{top:703px;left:60px;right:0;color:var(--white);font-size:14px}

/* back */
.back-photo{left:0;top:0;width:508px;height:192px;background:linear-gradient(180deg,#1f5a22 0%,#3b8a2f 50%,#7cbf44 100%)}
.brand-back{top:48px;left:150px;display:flex;align-items:center;gap:10px}
.brand-back .brand-dot{background:var(--white);width:28px;height:28px}
.brand-back .brand-name{color:var(--white);font-size:34px}
.band-yellow{top:192px;height:27px;background:var(--yellow);color:var(--white);font-family:'Asap',sans-serif;font-size:22px;line-height:27px;white-space:nowrap}
.band-yellow b{font-weight:700}
.band-blue{top:219px;height:73px;background:var(--blue);color:var(--white);font-size:12.5px;line-height:14.6px;padding-top:7px;white-space:nowrap}
.band-blue b{font-family:'Asap',sans-serif}
.h-brown{font-family:'Asap',sans-serif;font-weight:700;font-size:21px;color:var(--brown)}
.body-text{font-size:12px;line-height:14.6px;color:#555;white-space:nowrap}
.band-grey{top:380px;height:103px;background:var(--grey-band)}
.h-green{font-family:'Asap',sans-serif;font-weight:700;font-size:21px;color:var(--green-dark)}
.caps{font-size:9.5px;line-height:12px;color:#444;text-transform:uppercase;white-space:nowrap}
.services{font-family:'Asap',sans-serif;font-weight:700;font-size:13px;line-height:14.6px;color:var(--blue);white-space:nowrap}
.cta-pill{left:73px;top:495px;width:364px;height:51px;padding-top:7px}
.cta-line{display:block;font-family:'Oswald',sans-serif;font-weight:500;font-size:13px;line-height:17px}
.cta-call{display:block;font-family:'Asap',sans-serif;font-weight:700;font-size:16px;line-height:19px}
.thumb{position:absolute;top:559px;width:104px;height:73px;border-radius:3px;border:2px solid #3e8b2b;background:linear-gradient(180deg,#6e9a56 0%,#4e9a34 45%,#86c74a 100%)}
.back-foot{top:642px;height:78px;background:var(--blue)}
.testi-pill{position:absolute;left:195px;top:655px;width:124px;height:19px;border-radius:8px;background:#3cb34a;color:var(--white);font-family:'Asap',sans-serif;font-weight:700;font-size:12px;line-height:19px;text-align:center}
.testi{top:680px;left:30px;right:30px;color:var(--white);font-size:11px;line-height:13.4px;text-align:center}
</style>
</head>
<body>

<section class="page page--front">
  <div class="photo front-photo" role="img" aria-label="Photo of a striped green lawn in a garden with hedges and flower borders"></div>
  <svg class="front-waves" width="508" height="150" viewBox="0 0 508 150">
    <path d="M0 150 L0 95 C90 20 170 30 260 55 C360 85 430 60 508 0 L508 150 Z" fill="#fff"/>
    <path d="M0 92 C90 20 170 28 260 52 C360 80 430 55 508 -2 L508 30 C430 85 360 100 260 75 C170 50 90 40 0 110 Z" fill="var(--brown)"/>
    <path d="M0 112 C90 44 170 54 260 78 C360 104 430 88 508 34 L508 46 C430 100 360 116 260 92 C170 68 90 60 0 124 Z" fill="var(--blue)"/>
  </svg>

  <div class="abs brand-front">
    <span class="brand-dot"></span>
    <span class="brand-name">Bramblewick Co</span>
  </div>

  <div class="rule" style="top:436px"></div>
  <div class="abs center tagline" style="top:439px">
    <div class="blue">TREATMENTS AND ADVICE</div>
    <div class="brown">TO KEEP YOUR LAWN LOOKING NICE</div>
  </div>
  <div class="rule" style="top:496px"></div>

  <div class="abs center new-area">BRAND NEW TO THE AREA!</div>

  <div class="pill exp-pill">
    8 YEARS <b>EXPERIENCE</b> MAINTAINING<br><b>THE FINEST LAWNS OF CHESHIRE</b>
  </div>

  <svg class="front-foot" width="508" height="80" viewBox="0 0 508 80">
    <path d="M120 10 C250 40 380 40 508 6 L508 16 C380 48 250 46 120 20 Z" fill="var(--green)"/>
    <path d="M60 6 C160 28 220 34 300 36 L300 40 C220 40 150 34 60 14 Z" fill="var(--yellow)"/>
    <path d="M0 30 C140 10 330 60 508 22 L508 80 L0 80 Z" fill="var(--blue)"/>
  </svg>

  <div class="seal" role="img" aria-label="Satisfaction guarantee badge"></div>

  <div class="contact">
    <svg width="22" height="36" viewBox="0 0 22 36"><rect x="1.5" y="1.5" width="19" height="33" rx="4" fill="none" stroke="var(--blue)" stroke-width="3"/><rect x="5" y="6" width="12" height="20" fill="var(--blue)"/><circle cx="11" cy="30" r="1.8" fill="var(--blue)"/></svg>
    <div class="contact-lines">
      <div><b>CALL TODAY-</b>01632 960418</div>
      <div style="padding-left:25px"><b>TEXT-</b> 07700 900562</div>
    </div>
  </div>

  <div class="abs center book">TO BOOK YOUR LAWN SURVEY</div>
  <div class="abs center web">&#9679; bramblewickco.co.uk</div>
</section>

<section class="page page--back">
  <div class="photo back-photo" role="img" aria-label="Photo of a striped lawn beside a garden path and white summer house"></div>
  <div class="abs brand-back">
    <span class="brand-dot"></span>
    <span class="brand-name">Bramblewick Co</span>
  </div>

  <div class="abs center band-yellow">FOR A BEAUTIFUL <b>WEED-FREE LAWN</b></div>
  <div class="abs center band-blue">
    Call Bramblewick Co today and start your journey to a wonderful, lush,<br>
    green lawn you and your family can enjoy.<br>
    Arrange a no-obligation lawn survey and quotation at a time to suit you.<br>
    <b>Call 01632 960418 now.</b>
  </div>

  <div class="abs center h-brown" style="top:298px">I WILL UNDERSTAND YOUR LAWN</div>
  <div class="abs center body-text" style="top:324px">
    Every lawn is unique. I take time to gain a comprehensive understanding<br>
    of your lawn and its situation. I will also listen to you and understand your<br>
    problems and your aspirations for your grass.
  </div>

  <div class="abs center band-grey"></div>
  <div class="abs center h-green" style="top:384px">INDUSTRY-LEADING LAWN CARE</div>
  <div class="abs center caps" style="top:408px">
    I have 8 years of experience in the leading edge of domestic lawn care.<br>
    I have a comprehensive range of treatments including:
  </div>
  <div class="abs center services" style="top:436px">
    Scarification | Aeration | Moss Control<br>
    Overseeding | Top Dressing | Lawn Repairs | Fertilisation &amp; Weed Control<br>
    Pest and Disease Management | Special Event Preparation
  </div>

  <div class="pill cta-pill">
    <span class="cta-line">SAVE TIME AND MONEY AND LEAVE YOUR LAWN TO AN EXPERT.</span>
    <span class="cta-call">CALL 01632 960418 TODAY.</span>
  </div>

  <div class="thumb" style="left:26px" role="img" aria-label="Photo of a garden lawn"></div>
  <div class="thumb" style="left:142px" role="img" aria-label="Photo of a striped lawn"></div>
  <div class="thumb" style="left:259px" role="img" aria-label="Photo of a lawn with shrubs"></div>
  <div class="thumb" style="left:378px" role="img" aria-label="Photo of a freshly mown lawn"></div>

  <div class="abs center back-foot"></div>
  <div class="testi-pill">TESTIMONIALS</div>
  <div class="abs testi">
    Your company have been fantastic. Reliable, good advice, effective treatments and you are
    very knowledgeable about lawns. You really do know what you are talking about! Cannot
    recommend you highly enough. - Dan
  </div>
</section>

</body>
</html>
```